Real Estate Investor needs awesome business card design

I invest in real estate, focused on multi-family properties, and I need a business card to hand out to potential partners. I prefer simple, clean designs, but it needs to stand out, so I'd like there to be a bit of red in the design as well.

It should include this information:

Front
Dallin Pecksworth
Real Estate Investor
Direct phone: 502-867-3394
Email: dallinhpecksworth@quillmail.example
Headshot (Picture), I've uploaded a few, just pick the one you think looks best with your design. You can remove the background from the headshot image if it looks better.

Back
The back of the card's design should flow and be congruent with the front. On the back I want to put an inspirational quote or question. There will be different ones depending on the card, so I'll need the original file so I can edit it in the end.

For now, use “The Pessimist Sees Difficulty In Every Opportunity. The Optimist Sees The Opportunity In Every Difficulty.” -Barnaby Ellsworth

Target Market(s)

Investors

Industry/Entity Type

Real Estate

Contact Information for Business Card

Front
Dallin Pecksworth
Real Estate Investor

Back
The back of the card's design should flow and be congruent with the front. On the back I want to put an inspirational quote or question. There will be different ones depending on the card, so I'll need the original file so I can edit it in the end. I've uploaded some EXAMPLES of business cards with quotes on them. Don't copy but feel free to use them as inspiration.

The design will be printed on "ZIB sized" business cards
1039 x 697 pixels
with rounded corners

Font styles to use
Serif
Decorative
Script

Colors
ec1f27

Requirements
Must have
• Headshot, name, and other information in it.
• 1039 x 697 pixels
• Rounded corners
• Clean design that pops. I'm open to see any color background, including black.
• Headshots can be located here: https://www.filecrate.example/sh/8kd2wq7mzt31hvx/BBQTXP4ruf9LmQ0KhcvWx7b?dl=0
Nice to have
• It would be awesome if the design included a personal signature or monogram, but if not I'll get a personal logo developed later and the card redesigned if I think it needs it.
Should not have
• Cluttered design

```html
<!DOCTYPE html>
<html lang="en">
<head>
<meta charset="utf-8">
<title>Quote Card – Back</title>
<link rel="stylesheet" href="https://fonts.googleapis.com/css2?family=Source+Sans+3:wght@400;500&family=Lobster&display=swap">
<style>
  :root {
    --bg-deep: #050b2e;
    --bg-mid: #0b1a5e;
    --ink-white: #ffffff;
    --ink-red: #c4101a;
    --ink-yellow: #ffd400;
    --ink-muted: #3a4150;
    --quote-mark: #4d5566;
  }
  html, body {
    margin: 0;
    padding: 0;
    width: 1200px;
    height: 805px;
    overflow: hidden;
    background: var(--bg-deep);
  }
  .card-back {
    position: relative;
    width: 1200px;
    height: 805px;
    overflow: hidden;
    background: radial-gradient(ellipse 60% 65% at 52% 42%, var(--bg-mid) 0%, #081452 45%, var(--bg-deep) 100%);
    font-family: "Source Sans 3", "Myriad Pro", sans-serif;
    font-weight: 500;
    color: var(--ink-white);
  }
  .skyline-art {
    position: absolute;
    left: 440px;
    top: 600px;
    width: 760px;
    height: 205px;
    background: radial-gradient(ellipse 55% 60% at 55% 75%, rgba(22, 44, 130, 0.45) 0%, rgba(22, 44, 130, 0.18) 55%, rgba(22, 44, 130, 0) 100%);
  }
  .quote-line {
    position: absolute;
    left: 0;
    width: 1200px;
    text-align: center;
    white-space: nowrap;
    line-height: 1;
    margin: 0;
  }
  .line-1 { top: 160px; font-size: 50px; padding-left: 20px; }
  .line-2 { top: 253px; font-size: 54px; padding-left: 20px; }
  .line-3 { top: 388px; font-size: 50px; padding-left: 20px; }
  .line-4 { top: 480px; font-size: 54px; padding-left: 20px; }
  .keyword {
    font-size: 92px;
    vertical-align: -6px;
  }
  .accent-red { color: var(--ink-red); }
  .accent-yellow { color: var(--ink-yellow); }
  .quote-mark {
    position: absolute;
    font-family: "Source Sans 3", sans-serif;
    font-style: italic;
    font-size: 70px;
    color: var(--quote-mark);
    line-height: 1;
  }
  .quote-open { left: 272px; top: 152px; }
  .quote-close { left: 995px; top: 455px; }
  .attribution {
    position: absolute;
    left: 0;
    top: 562px;
    width: 1200px;
    margin: 0;
    text-align: center;
    font-family: "Lobster", cursive;
    font-size: 38px;
    letter-spacing: 1px;
    line-height: 1;
    color: var(--ink-muted);
    padding-left: 20px;
  }
</style>
</head>
<body>
  <main class="card-back">
    <div class="skyline-art" role="img" aria-label="Faint illustration of a row of houses along the bottom edge"></div>

    <span class="quote-mark quote-open">“</span>

    <div class="quote-line line-1">The <span class="keyword accent-red">Pessimist</span> Sees</div>
    <div class="quote-line line-2"><span class="accent-red">Difficulty</span> In Every Opportunity.</div>
    <div class="quote-line line-3">The <span class="keyword accent-yellow">Optimist</span> Sees The</div>
    <div class="quote-line line-4"><span class="accent-yellow">Opportunity</span> In Every Difficulty.</div>

    <span class="quote-mark quote-close">”</span>

    <p class="attribution">Barnaby Ellsworth</p>
  </main>
</body>
</html>
```